Need a Halden & Co
* logo
* word and powerpoint livery
* basic webpage

Halden & Co is a Private M&A Advisor. We want to look like http://www.brightwickadvisory.example
It needs to communicate reliabity, conservativeness and discretion.

```html
<!DOCTYPE html>
<html lang="en">
<head>
<meta charset="utf-8">
<title>Halden & Co</title>
<link href="https://fonts.googleapis.com/css2?family=Open+Sans:wght@400;600;700&family=Roboto:wght@300;400&display=swap" rel="stylesheet">
<style>
:root{
  --blue:#0a86b8;
  --blue-dark:#05628c;
  --nav-top:#0f8dbd;
  --nav-bottom:#0272a2;
  --text:#222;
  --muted:#666;
  --footer:#13212b;
  --footer-text:#c9d0d5;
  --line:#e2e2e2;
}
*{margin:0;padding:0;box-sizing:border-box}
html,body{width:1200px;height:1140px;overflow:hidden;background:#fff}
body{position:relative;font-family:"Open Sans",sans-serif;color:var(--text)}
.top-rule{position:absolute;left:0;top:0;width:1200px;height:2px;background:var(--blue)}
.brand{position:absolute;left:181px;top:36px;font:700 23px/30px "Open Sans",sans-serif;color:var(--blue);letter-spacing:.2px}
.search{position:absolute;left:743px;top:30px;width:277px;height:40px;border:1px solid var(--line);font-size:12px;color:#888;padding:0 16px;line-height:38px}
.search svg{position:absolute;right:14px;top:12px}
.nav{position:absolute;left:181px;top:92px;width:839px;height:57px;background:linear-gradient(var(--nav-top),var(--nav-bottom));list-style:none}
.nav li{position:absolute;top:0;height:57px;line-height:57px;font-size:11.5px;color:#fff;transform:translateX(-50%);white-space:nowrap}
.nav li.active{left:0;transform:none;width:81px;text-align:center;background:var(--blue-dark)}
.slider{position:absolute;left:181px;top:149px;width:839px;height:379px;background:linear-gradient(100deg,#6f7479 0%,#b9b4ac 30%,#e7e4df 55%,#d6dde6 75%,#eceeef 100%)}
.caption{position:absolute;left:38px;top:280px;width:362px;height:70px;background:rgba(255,255,255,.78);font:400 21px/70px "Roboto",sans-serif;padding-left:18px;color:#1e2a33}
.dots{position:absolute;left:726px;top:345px;display:flex;gap:9px}
.dots span{width:14px;height:14px;background:#1b1b1b}
.dots span.on{background:var(--blue)}
.welcome{position:absolute;left:181px;top:557px;width:839px;text-align:center}
h2{font:300 21px/28px "Roboto",sans-serif;color:var(--blue)}
.welcome p{margin-top:9px;font-size:11.5px;line-height:20.5px;color:#555}
.col{position:absolute;top:675px}
.col h4{font-size:12.5px;font-weight:400;line-height:17px;text-transform:uppercase;color:#222;white-space:nowrap}
.col p{font-size:11.2px;line-height:17px;color:var(--muted)}
.col .thumb{position:absolute;left:0;top:41px;width:85px;height:67px}
.col .side{position:absolute;left:97px;top:38px;width:180px}
.news-title{position:absolute;left:181px;top:863px}
.news{position:absolute;top:905px;width:270px}
.date{position:absolute;left:0;top:0;width:57px;height:54px;background:var(--blue);color:#fff;text-align:center}
.date b{display:block;font:600 16px/22px "Open Sans",sans-serif;padding-top:5px}
.date span{font-size:12px;line-height:20px}
.news h4{margin-left:64px;font-size:12.8px;line-height:19px;font-weight:400;text-transform:uppercase;white-space:nowrap}
.news p{margin-top:8px;font-size:11.2px;line-height:15.5px;color:var(--muted)}
.footer{position:absolute;left:0;top:1041px;width:1200px;height:99px;background:var(--footer)}
.footer h3{position:absolute;left:179px;top:20px;font:300 15.5px/20px "Roboto",sans-serif;color:#fff}
.address{position:absolute;left:179px;top:48px;font-size:11px;line-height:15.5px;color:var(--footer-text)}
.social{position:absolute;left:868px;top:23px;display:flex;gap:7.5px}
.social span{width:19px;height:19px;border-radius:50%;border:1px solid rgba(255,255,255,.35)}
.copyright{position:absolute;right:182px;top:58px;font-size:11px;color:var(--footer-text)}
</style>
</head>
<body>
<div class="top-rule"></div>
<div class="brand">HALDEN &amp; CO</div>
<div class="search">Search...
  <svg width="14" height="14" viewBox="0 0 14 14"><circle cx="6" cy="6" r="4.6" fill="none" stroke="#bbb" stroke-width="1.5"/><line x1="9.4" y1="9.4" x2="13" y2="13" stroke="#bbb" stroke-width="1.5"/></svg>
</div>
<ul class="nav">
  <li class="active">HOME</li>
  <li style="left:133px">ABOUT</li>
  <li style="left:234px">SERVICES</li>
  <li style="left:336px">CAREER</li>
  <li style="left:429px">NEWS</li>
  <li style="left:531px">EXPERIENCE</li>
  <li style="left:636px">BLOG</li>
  <li style="left:743px">CONTACT US</li>
</ul>
<div class="slider" role="img" aria-label="Photo of an advisor meeting a young couple signing documents at a desk with building models">
  <div class="caption">We are a small investment bank</div>
  <div class="dots"><span></span><span></span><span class="on"></span><span></span></div>
</div>
<section class="welcome">
  <h2>WELCOME TO HALDEN &amp; CO</h2>
  <p>Ut wisi enim ad minim veniam, quis nostrud exerci tation ullamcorper suscipit lobortis nisl ut aliquip ex ea commodo consequat. Duis autem vel eum iriure dolor in hendrerit in vulputate velit esse molestie consequat, vel illum dolore eu feugiat nulla facilisis at vero eros et accumsan et iusto odio dignissim qui blandit prae sent luptatum zzril delenit augue duis dolore te feugait nulla facilisi.</p>
</section>
<div class="col" style="left:181px;width:260px">
  <h2>WHY CHOOSE US</h2>
  <h4 style="margin-top:10px;line-height:20.5px">Mes cuml dia sed ineniasinge dolor<br>commete ipsum comnetus.</h4>
  <p style="margin-top:2px">Dolor nunc vule putateulr ips dol consec.Donec semp ertet laciniate ultricie upien disse comete dolo lectus fgilla itollicil tua ludin dolor nec met quam accumsan dolore.</p>
</div>
<div class="col" style="left:457px;width:275px;height:170px">
  <h2>OUR EXPERIENCE</h2>
  <div class="thumb" role="img" aria-label="Photo of hands dropping coins into a piggy bank" style="background:linear-gradient(135deg,#8fb3d6,#d7dde6 60%,#e9c4cc)"></div>
  <h4 class="side">Lorem ipsum dolor sit<br>amet, consectetuer<br>adipis cing elit, sed diam<br>nonummy</h4>
  <p style="position:absolute;top:116px;width:275px">Ut wisi enim ad minim veniam, quis nostrud exerci tation ullamcorper suscipit lobortis nisl ut aliquip ex ea commodo consequat.</p>
</div>
<div class="col" style="left:748px;width:275px;height:170px">
  <h2>HOW WE CAN HELP</h2>
  <div class="thumb" role="img" aria-label="Photo of stacked banknotes" style="background:linear-gradient(135deg,#b79a8c,#d9cfc6 55%,#8c8b8a)"></div>
  <h4 class="side">Think of a secretive swiss<br>bank -</h4>
  <h4 class="side" style="top:80px">Secretive, solid, reliable</h4>
  <p style="position:absolute;top:116px;width:275px">Ut wisi enim ad minim veniam, quis nostrud exerci tation ullamcorper suscipit lobortis nisl ut aliquip ex ea commodo consequat.</p>
</div>
<h2 class="news-title">LATEST NEWS</h2>
<article class="news" style="left:181px">
  <div class="date"><b>29</b><span>AUG</span></div>
  <h4>Lorem ipsum dolor sit amet,<br>consectetuer adipiscing elit,<br>sed diam nonummy</h4>
  <p>Ut wisi enim ad minim veniam, quis nostrud exerci tation ullamcorper suscipit lobortis nisl ut aliquip ex ea commodo consequat...</p>
</article>
<article class="news" style="left:466px">
  <div class="date"><b>27</b><span>AUG</span></div>
  <h4>Ut wisi enim ad minim veniam,<br>quis nostrud exerci tation<br>ullamcorper suscipit</h4>
  <p>Ut wisi enim ad minim veniam, quis nostrud exerci tation ullamcorper suscipit lobortis nisl ut aliquip ex ea commodo consequat...</p>
</article>
<article class="news" style="left:753px">
  <div class="date"><b>25</b><span>AUG</span></div>
  <h4>Nam liber tempor cum<br>soluta nobis eleifend option<br>congue nihil</h4>
  <p>Ut wisi enim ad minim veniam, quis nostrud exerci tation ullamcorper suscipit lobortis nisl ut aliquip ex ea commodo consequat...</p>
</article>
<footer class="footer">
  <h3>OUR LOCATION</h3>
  <div class="address">4186 Lorem Ipsm. Lorem Ipsm,&nbsp; Lorem Ipsm 20461.<br>Tel +1-555-010-2468 Fax +1-555-010-3579</div>
  <div class="social" aria-label="Social links">
    <span style="background:#3b5a98"></span><span style="background:#2aa3df"></span><span style="background:#1b75b5"></span><span style="background:#c8302a"></span><span style="background:#e2692a"></span><span style="background:#d34836"></span>
  </div>
  <div class="copyright">Copyright @2014 Halden &amp; Co. All Right Reserved.</div>
</footer>
</body>
</html>
```